Salon website

Need a web design for a new blow dry and hair extension boutique in CT
would like the color scheme to be gray, white and tiffany blue
Create a web site with about 4 pages showing
1 about us page
1 blow dry services page
1 hair extension services page
1 contact us page
1 membership page
1 parties page

Industry/Entity Type

Boutique

Colors
86cfc6
cfeae6
33b7a4
aaaaaa
cbcbcb
ffffff

```html
<!DOCTYPE html>
<html lang="en">
<head>
<meta charset="utf-8">
<title>Velvet Blow — Blow Dry &amp; Hair Extension Boutique</title>
<link href="https://fonts.googleapis.com/css2?family=Open+Sans:wght@300;400;600;700&display=swap" rel="stylesheet">
<style>
:root{
  --tiffany:#86cfc6;
  --tiffany-pale:#cfeae6;
  --tiffany-deep:#33b7a4;
  --gray:#aaaaaa;
  --gray-light:#cbcbcb;
  --white:#ffffff;
  --page:#eeeeee;
  --ink:#3a3a3a;
  --muted:#8a8a8a;
  --dark:#222222;
}
*{box-sizing:border-box;margin:0;padding:0}
html,body{width:1200px;height:2888px;overflow:hidden}
body{font-family:"Open Sans",Arial,sans-serif;background:var(--page);color:var(--ink);position:relative}
.wrap{width:830px;margin:0 auto;position:relative}

/* header */
.site-header{height:100px;background:var(--tiffany);position:relative}
.brand{position:absolute;left:190px;top:14px;display:flex;flex-direction:column;align-items:center;gap:4px}
.brand-mark{width:50px;height:50px;border-radius:50%;background:var(--tiffany-pale)}
.brand-name{font-size:12px;font-weight:600;color:var(--white);letter-spacing:2px;text-transform:uppercase}
.tagline{position:absolute;left:0;right:0;top:14px;text-align:center;color:var(--white);font-size:17px;line-height:26px;font-weight:400}
.social{position:absolute;right:178px;top:12px;display:flex;gap:8px}
.social span{width:22px;height:22px;border-radius:50%;background:var(--tiffany-deep)}

/* nav */
.main-nav{height:60px;background:var(--tiffany-deep);display:flex;align-items:center;padding-left:200px;gap:34px}
.main-nav a{color:var(--white);text-decoration:none;font-size:13px;font-weight:700}
.main-nav a.active{border:2px solid var(--white);border-radius:6px;padding:5px 14px;background:rgba(255,255,255,.12)}

/* hero */
.hero{height:435px;background:linear-gradient(90deg,#c3e6e0,var(--tiffany-pale) 50%,#bfe4de);position:relative;overflow:hidden}
.hero-photo{position:absolute;left:560px;top:0;width:460px;height:435px;background:radial-gradient(ellipse at 60% 40%,#f2d6cf 0%,#e9b8c2 35%,#a8dad2 80%)}
.hero-text{position:absolute;left:210px;top:160px;width:760px;text-align:center;font-size:28px;line-height:40px;font-weight:400;color:var(--white);text-shadow:0 1px 3px rgba(0,0,0,.35)}
.hero-arrow{position:absolute;top:200px}
.hero-arrow.prev{left:160px}.hero-arrow.next{right:160px}
.hero-dots{position:absolute;bottom:18px;left:0;right:0;display:flex;justify-content:center;gap:7px}
.hero-dots span{width:7px;height:7px;border-radius:50%;background:rgba(255,255,255,.6)}
.hero-dots span.on{background:var(--white)}

/* services */
.services{padding-top:30px;height:440px}
.services.hair{height:430px;padding-top:16px}
.section-head{display:flex;justify-content:space-between;align-items:center;border-bottom:1px solid var(--gray-light);padding-bottom:8px;margin-bottom:14px}
.section-head h2{font-size:16px;font-weight:700;color:var(--ink);text-transform:uppercase}
.btn-outline{font-size:9px;color:var(--muted);border:1px solid var(--gray-light);border-radius:10px;padding:3px 10px;background:var(--white)}
.cards{display:flex;justify-content:space-between}
.card{width:260px;position:relative}
.card-photo{height:228px;display:block}
.card h3{font-size:13px;font-weight:700;margin:12px 0 6px;color:var(--ink)}
.card p{font-size:10px;line-height:15px;color:var(--muted)}
.card .more{display:flex;justify-content:flex-end;margin-top:6px}
.btn-more{font-size:9px;color:var(--ink);border:1px solid var(--gray-light);border-radius:8px;padding:2px 9px;background:var(--white)}
.badge-new{position:absolute;top:-12px;right:-6px;width:42px;height:42px;border-radius:50%;background:var(--tiffany);color:var(--white);font-size:10px;font-weight:700;display:flex;align-items:center;justify-content:center;border:3px solid var(--white)}

/* quotes */
.quote{height:250px;border-top:1px solid #dcdcdc;text-align:center;padding-top:50px}
.quote h2{font-size:28px;line-height:40px;font-weight:300;color:#6f6f6f;width:720px;margin:0 auto}
.quote p{font-size:10px;line-height:15px;color:var(--muted);width:560px;margin:26px auto 12px}
.quote-dots{display:flex;justify-content:center;gap:6px}
.quote-dots span{width:12px;height:12px;border-radius:50%;border:2px solid var(--tiffany-deep)}
.quote-dots span.on{background:var(--tiffany-deep)}

/* testimonials */
.testimonials{position:absolute;top:2040px;left:0;width:1200px;height:455px;background:var(--tiffany-deep);color:var(--white)}
.testimonials h2{font-size:18px;font-weight:700;padding:22px 0 8px;border-bottom:1px solid rgba(255,255,255,.45);margin-bottom:34px}
.t-cols{display:flex;justify-content:space-between;padding:0 10px}
.t-item{width:300px}
.avatar{width:115px;height:115px;border-radius:50%;border:4px solid var(--white);display:block;margin-bottom:18px}
.t-item h3{font-size:16px;font-weight:700}
.t-item h4{font-size:12px;font-weight:600;margin-bottom:10px}
.t-item p{font-size:11px;line-height:16px}

/* footer */
.site-footer{position:absolute;top:2495px;left:0;width:1200px;height:345px;background:var(--gray)}
.f-cols{display:flex;padding-top:40px;gap:0}
.f-col{color:var(--white)}
.f-col h3{font-size:15px;font-weight:700;padding-bottom:6px;border-bottom:1px solid rgba(255,255,255,.6);margin-bottom:10px;text-transform:uppercase}
.f-col li{list-style:none;font-size:11px;line-height:16px}
.f-col.links li{font-size:9px;line-height:14px;margin-bottom:10px}
.copyright{position:absolute;top:2840px;left:0;width:1200px;height:48px;background:var(--dark);color:#bbb;font-size:9px;display:flex;align-items:center;justify-content:center}
</style>
</head>
<body>

<header class="site-header">
  <div class="brand"><span class="brand-mark"></span><span class="brand-name">Velvet Blow</span></div>
  <p class="tagline">Eum brute illud prompta ne, nec molestiae<br>efficiantur suscipiantur an</p>
  <div class="social"><span></span><span></span></div>
</header>

<nav class="main-nav">
  <a class="active" href="#">Home</a>
  <a href="#">About Us</a>
  <a href="#">Blow Dry Services</a>
  <a href="#">Hair Extension Services</a>
  <a href="#">Contact Us</a>
  <a href="#">Membership</a>
  <a href="#">Parties</a>
</nav>

<section class="hero">
  <div class="hero-photo" role="img" aria-label="Beauty portrait with flowers in the hair and butterflies"></div>
  <svg class="hero-arrow prev" width="16" height="30" viewBox="0 0 16 30"><path d="M13 3 3 15l10 12" fill="none" stroke="#fff" stroke-width="3"/></svg>
  <svg class="hero-arrow next" width="16" height="30" viewBox="0 0 16 30"><path d="M3 3l10 12L3 27" fill="none" stroke="#fff" stroke-width="3"/></svg>
  <p class="hero-text">Eum brute illud prompta ne, nec molestiae efficiantur suscipiantur an. Amet congue diceret nec</p>
  <div class="hero-dots"><span class="on"></span><span></span><span></span><span></span></div>
</section>

<main>
  <section class="services wrap">
    <div class="section-head"><h2>Blow Dry Services</h2><span class="btn-outline">See all of our offers</span></div>
    <div class="cards">
      <article class="card">
        <div class="card-photo" role="img" aria-label="Woman with smooth skin touching her face" style="background:linear-gradient(160deg,#fafafa,#ead9cf 60%,#f4f4f4)"></div>
        <h3>Vestibulum convallis hendrerit</h3>
        <p>Lorem ipsum dolor sit amet, consectetur adipiscing elit. Sed nec interdum ante. Duis accumsan ultricies felis eget porta. Maecenas hendrerit enim purus.</p>
        <div class="more"><span class="btn-more">Read More</span></div>
      </article>
      <article class="card">
        <span class="badge-new">NEW</span>
        <div class="card-photo" role="img" aria-label="Woman with sleek dark hair in profile" style="background:linear-gradient(160deg,#f6f6f6,#e6d3c8 55%,#f1f1f1)"></div>
        <h3>Vestibulum convallis hendrerit</h3>
        <p>Lorem ipsum dolor sit amet, consectetur adipiscing elit. Sed nec interdum ante. Duis accumsan ultricies felis eget porta. Maecenas hendrerit enim purus.</p>
        <div class="more"><span class="btn-more">Read More</span></div>
      </article>
      <article class="card">
        <div class="card-photo" role="img" aria-label="Woman with glossy blow dried hair on dark background" style="background:linear-gradient(160deg,#2a2a2e,#6b5a55 55%,#1e1e22)"></div>
        <h3>Vestibulum convallis hendrerit</h3>
        <p>Lorem ipsum dolor sit amet, consectetur adipiscing elit. Sed nec interdum ante. Duis accumsan ultricies felis eget porta. Maecenas hendrerit enim purus.</p>
        <div class="more"><span class="btn-more">Read More</span></div>
      </article>
    </div>
  </section>

  <section class="services hair wrap">
    <div class="section-head"><h2>Hair Extension Services</h2><span class="btn-outline">See all of our offers</span></div>
    <div class="cards">
      <article class="card">
        <div class="card-photo" role="img" aria-label="Woman with long dark hair holding a red flower" style="background:linear-gradient(160deg,#3a2e2e,#7a4a4a 50%,#2b2323)"></div>
        <h3>Vestibulum convallis hendrerit</h3>
        <p>Lorem ipsum dolor sit amet, consectetur adipiscing elit. Sed nec interdum ante. Duis accumsan ultricies felis eget porta. Maecenas hendrerit enim purus.</p>
        <div class="more"><span class="btn-more">Read More</span></div>
      </article>
      <article class="card">
        <div class="card-photo" role="img" aria-label="Woman with voluminous blonde curls" style="background:linear-gradient(160deg,#4a3b28,#d9b878 50%,#5a4630)"></div>
        <h3>Vestibulum convallis hendrerit</h3>
        <p>Lorem ipsum dolor sit amet, consectetur adipiscing elit. Sed nec interdum ante. Duis accumsan ultricies felis eget porta. Maecenas hendrerit enim purus.</p>
        <div class="more"><span class="btn-more">Read More</span></div>
      </article>
      <article class="card">
        <div class="card-photo" role="img" aria-label="Woman with long wavy auburn hair extensions" style="background:linear-gradient(160deg,#d8a27a,#a4603f 55%,#e3c1a0)"></div>
        <h3>Vestibulum convallis hendrerit</h3>
        <p>Lorem ipsum dolor sit amet, consectetur adipiscing elit. Sed nec interdum ante. Duis accumsan ultricies felis eget porta. Maecenas hendrerit enim purus.</p>
        <div class="more"><span class="btn-more">Read More</span></div>
      </article>
    </div>
  </section>

  <section class="quote">
    <h2>Eum brute illud prompta ne, nec molestiae efficiantur suscipiantur an. Amet congue diceret nec</h2>
    <p>Lorem ipsum dolor sit amet, consectetur adipiscing elit. Sed nec interdum ante. Duis accumsan ultricies felis eget porta. Maecenas hendrerit enim purus, semper volutpat nibh dapibus eget.</p>
    <div class="quote-dots"><span class="on"></span><span></span><span></span></div>
  </section>

  <section class="quote">
    <h2>Eum brute illud prompta ne, nec molestiae efficiantur suscipiantur an. Amet congue diceret nec</h2>
    <p>Lorem ipsum dolor sit amet, consectetur adipiscing elit. Sed nec interdum ante. Duis accumsan ultricies felis eget porta. Maecenas hendrerit enim purus, semper volutpat nibh dapibus eget.</p>
    <div class="quote-dots"><span class="on"></span><span></span></div>
  </section>
</main>

<section class="testimonials">
  <div class="wrap">
    <h2>Testimonials</h2>
    <div class="t-cols">
      <div class="t-item">
        <div class="avatar" role="img" aria-label="Customer portrait" style="background:linear-gradient(160deg,#e8d2c2,#9c6b4e)"></div>
        <h3>Customer Name</h3>
        <h4>Company Name</h4>
        <p>"Lorem ipsum dolor sit amet, consectetur adipiscing elit. Sed nec interdum ante. Duis accumsan ultricies felis eget porta. Maecenas hendrerit enim purus, semper volutpat nibh dapibus eget. In eleifend interdum condimentum."</p>
      </div>
      <div class="t-item">
        <div class="avatar" role="img" aria-label="Customer portrait" style="background:linear-gradient(160deg,#e6cdb9,#7a4f3a)"></div>
        <h3>Customer Name</h3>
        <h4>Company Name</h4>
        <p>"Lorem ipsum dolor sit amet, consectetur adipiscing elit. Sed nec interdum ante. Duis accumsan ultricies felis eget porta. Maecenas hendrerit enim purus, semper volutpat nibh dapibus eget. In eleifend interdum condimentum."</p>
      </div>
    </div>
  </div>
</section>

<footer class="site-footer">
  <div class="wrap f-cols">
    <div class="f-col" style="width:190px;margin-right:0"><h3 style="width:140px">Information</h3>
      <ul><li>Specials</li><li>New products</li><li>Best sellers</li><li>Our stores</li><li>Contact us</li><li>Terms and conditions</li><li>of use</li><li>About us</li><li>Sitemap</li></ul></div>
    <div class="f-col" style="width:210px"><h3 style="width:160px">Extras</h3>
      <ul><li>Brands</li><li>Specials</li><li>New products</li><li>Top sellers</li></ul></div>
    <div class="f-col" style="width:195px"><h3 style="width:160px">My Account</h3>
      <ul><li>My orders</li><li>My credit slips</li><li>My addresses</li><li>My personal info</li></ul></div>
    <div class="f-col links" style="width:235px"><h3>Links</h3>
      <ul><li>How Trends Put The Bounce Back</li><li>Styles With Life In Your Hair</li><li>What Is A Good Salon Routine</li><li>Seven Tips For Healthy Lengths</li><li>Make Your Blowout Last Longer</li></ul></div>
  </div>
</footer>
<div class="copyright">Copyright 2013 Salon Website</div>

</body>
</html>
```